2016 Ashbury Animal League Calendar contest

We are looking for a banner -width (920px) to engage people to enter our 2016 Calendar contest. We are a Canadian non-profit, who rescues over 8,000 animals a year.
Our Calendar is very popular, and I have had many people contact me wanting their pet featured in next year's calendar. The contest will run from Nov.1 to Feb. 1 at which time our photographer will take photos of the winning pets for the calendar.

Our calendar features actual AAL pets who were adopted from our shelter and includes their photo and before/after story.

Make your Pet a Star!!
Contest Description:
Did you adopt your furry friend from The Ashbury Animal League? Want your AAL animal featured in next year’s calendar? Enter our Calendar Contest Today!
Every person who enters will have their own fundraising page, and the individuals with the most votes(donations) will be featured in the 2016 calendar.

I am attaching the calendars from the last 3 years so you can get a feel for what they look like. I also attached our logo and some individual pictures of the animals featured.

920 W x 260 H You can use the graphics from previous calendar or keep it simple, wouldn't mind to see different ideas!

The banner is primarily for our calendar contest page: http://www.fundloopa.com/projects/2016-aal-calendar-contest/ The rules of the contest are listed on the page. I wouldn't mind seeing a banner with one call to action- Enter our Contest. (attaching an example of another org who did something similar)

Requirements
Must have
• Also, Make sure the designer provides you a PNG 32 file with transparent rounded corners to fit better on your page.
Should not have
• Too much text! Keep it simple!
Secure YOUR spot at the 2016 calendar today!
or Enter Today!

Have the call to action "make our pet a star" the top and dominant language.

```html
<!DOCTYPE html>
<html lang="en">
<head>
<meta charset="utf-8">
<title>Make Your Pet a Star – 2016 Calendar Contest</title>
<link href="https://fonts.googleapis.com/css2?family=Oswald:wght@500&family=Raleway:wght@300;400;700&family=Roboto:wght@400&display=swap" rel="stylesheet">
<style>
  :root {
    --green-deep: #3f7a16;
    --green-mid: #6aa621;
    --green-light: #a9d44a;
    --green-glow: #d3ec8a;
    --lime: #c6e84a;
    --badge-dark: #1f2224;
    --badge-ring: #2c3033;
    --white: #ffffff;
    --fur-light: #d9a25a;
    --fur-mid: #b9722c;
    --fur-dark: #7a4516;
    --league-green: #2f8a2a;
  }
  html, body {
    margin: 0;
    padding: 0;
    width: 1200px;
    height: 339px;
    overflow: hidden;
    background: #ffffff;
  }
  .banner {
    position: relative;
    width: 1200px;
    height: 339px;
    overflow: hidden;
    background:
      radial-gradient(ellipse 300px 200px at 620px 60px, rgba(211,236,138,0.55), transparent 70%),
      radial-gradient(ellipse 260px 240px at 80px 300px, rgba(63,122,22,0.55), transparent 70%),
      radial-gradient(ellipse 380px 260px at 980px 120px, rgba(211,236,138,0.6), transparent 70%),
      linear-gradient(160deg, var(--green-mid) 0%, var(--green-light) 45%, var(--green-mid) 75%, var(--green-deep) 100%);
    font-family: "Raleway", sans-serif;
    color: var(--white);
  }
  .dotted-rule {
    position: absolute;
    height: 0;
    border-top: 4px dotted rgba(255,255,255,0.9);
  }
  .dotted-rule.top { left: 241px; width: 660px; top: 16px; }
  .dotted-rule.under { left: 248px; width: 600px; top: 122px; }

  .entry-badge {
    position: absolute;
    left: 10px;
    top: 26px;
    width: 212px;
    height: 212px;
  }
  .entry-badge-text {
    position: absolute;
    left: 10px;
    top: 26px;
    width: 212px;
    height: 212px;
    display: flex;
    flex-direction: column;
    align-items: center;
    justify-content: center;
    font-family: "Raleway", sans-serif;
    font-weight: 300;
    font-size: 31px;
    line-height: 1.02;
    text-align: center;
    text-transform: uppercase;
    transform: rotate(-12deg);
  }
  .entry-badge-text .accent {
    color: var(--lime);
    font-weight: 700;
    font-size: 35px;
  }

  .headline {
    position: absolute;
    left: 352px;
    top: 36px;
    margin: 0;
    font-family: "Oswald", sans-serif;
    font-weight: 500;
    font-size: 60px;
    line-height: 76px;
    letter-spacing: 1px;
    text-transform: uppercase;
    text-shadow: 0 2px 6px rgba(0,0,0,0.25);
  }
  .subhead {
    position: absolute;
    left: 340px;
    top: 132px;
    margin: 0;
    font-weight: 300;
    font-size: 42px;
    line-height: 46px;
    text-shadow: 0 2px 5px rgba(0,0,0,0.2);
  }
  .subhead strong { font-weight: 700; }
  .subhead .line-two { display: block; padding-left: 50px; }

  .contest-note {
    position: absolute;
    left: 280px;
    top: 239px;
    width: 632px;
    height: 86px;
    box-sizing: border-box;
    border: 1px solid rgba(255,255,255,0.75);
    background: rgba(40,70,10,0.35);
    display: flex;
    align-items: center;
    justify-content: center;
    text-align: center;
    font-family: "Roboto", sans-serif;
    font-size: 13.5px;
    line-height: 16px;
    padding: 4px 10px;
  }
  .contest-note::before {
    content: "";
    position: absolute;
    left: -8px;
    top: -8px;
    width: 120px;
    height: 40px;
    border-top: 1px solid rgba(255,255,255,0.6);
    border-left: 1px solid rgba(255,255,255,0.6);
  }

  .pet-photo {
    position: absolute;
    left: 840px;
    top: -20px;
    width: 400px;
    height: 380px;
    background:
      radial-gradient(ellipse 150px 170px at 190px 200px, var(--fur-mid), transparent 75%),
      radial-gradient(ellipse 200px 220px at 220px 190px, rgba(217,162,90,0.9), transparent 80%),
      radial-gradient(ellipse 240px 260px at 240px 200px, rgba(122,69,22,0.35), transparent 85%);
  }

  .league-mark {
    position: absolute;
    left: 1064px;
    top: 300px;
    width: 132px;
    display: flex;
    align-items: center;
    gap: 5px;
    font-family: "Raleway", sans-serif;
    font-weight: 700;
    font-size: 9.5px;
    line-height: 11px;
    text-transform: uppercase;
    color: var(--league-green);
  }
  .league-mark .dot {
    flex: 0 0 auto;
    width: 12px;
    height: 12px;
    border-radius: 50%;
    background: var(--league-green);
  }
</style>
</head>
<body>
<div class="banner">
  <div class="dotted-rule top"></div>

  <svg class="entry-badge" viewBox="0 0 212 212" aria-hidden="true">
    <circle cx="106" cy="106" r="104" fill="none" stroke="rgba(255,255,255,0.55)" stroke-width="2"/>
    <circle cx="106" cy="106" r="96" fill="var(--badge-ring)"/>
    <circle cx="106" cy="106" r="86" fill="none" stroke="var(--lime)" stroke-width="7" stroke-dasharray="2 3"/>
    <circle cx="106" cy="106" r="76" fill="var(--badge-dark)" stroke="rgba(255,255,255,0.2)" stroke-width="2"/>
  </svg>
  <div class="entry-badge-text">
    <span>Enter</span>
    <span class="accent">Your</span>
    <span class="accent">Pet</span>
    <span>Today!</span>
  </div>

  <h1 class="headline">Make Your Pet a Star!!</h1>
  <div class="dotted-rule under"></div>

  <h2 class="subhead">Secure <strong>YOUR</strong> spot <span class="line-two">at the <strong>2016 Calendar</strong></span></h2>

  <p class="contest-note">
    Did you adopt your furry friend from The Ashbury Animal League?<br>
    Want your AAL animal featured in next year’s calendar?<br>
    Enter our Calendar Contest Today!<br>
    Every person who enters will have their own fundraising page,<br>
    and the individuals with the most votes(donations) will be featured in the 2016 calendar.
  </p>

  <div class="pet-photo" role="img" aria-label="Photo of a happy fluffy orange small dog, adopted from the shelter"></div>

  <div class="league-mark">
    <span class="dot"></span>
    <span>The Ashbury Animal League</span>
  </div>
</div>
</body>
</html>
```